Bettinas Professional Resume

Pls upgrade to make look more effective and perhaps add α photo on it, both options with photo and without would be great. Thanks very much. I would also like the resume so I can edit as well if I need to down the track.

This is my professional resume to make it more effective to potential senior hiring managers,

f04a50

• Professional look.

```html
<!DOCTYPE html>
<html lang="en">
<head>
<meta charset="utf-8">
<title>Bettinas Professional Resume</title>
<link href="https://fonts.googleapis.com/css2?family=Great+Vibes&family=Source+Sans+3:ital,wght@0,400;0,600;0,700;1,400&display=swap" rel="stylesheet">
<style>
:root{
  --red:#f04a50;
  --bg:#3a3a3e;
  --tagbar:#9b9b9b;
  --panel:#efefef;
  --ink:#231f20;
  --muted:#6d6d6d;
  --white:#ffffff;
  --ring:#d9d9d9;
}
*{margin:0;padding:0;box-sizing:border-box}
html,body{width:1200px;height:568px;overflow:hidden;background:var(--bg)}
body{position:relative;font-family:"Source Sans 3",Arial,sans-serif;color:var(--ink)}
.page{position:absolute;top:52px;width:329px;height:465px;background:var(--white);overflow:hidden;box-shadow:0 4px 14px rgba(0,0,0,.45)}
.page--photo{left:73px}
.page--plain{left:435px}
.page--experience{left:800px}
.page__footer{position:absolute;left:0;right:0;bottom:0;height:6px;background:var(--red)}
.abs{position:absolute}

/* header */
.header-red{position:absolute;left:0;top:0;height:72px;background:var(--red)}
.header-light{position:absolute;left:126px;top:0;width:203px;height:72px;background:var(--panel)}
.photo{position:absolute;left:35px;top:5px;width:61px;height:61px;border-radius:50%;border:2.5px solid var(--white);background:radial-gradient(circle at 50% 40%,#e6e1dc 0%,#b9aca4 55%,#3b2f2c 100%)}
.script-name{font-family:"Great Vibes",cursive;font-weight:400;white-space:nowrap;text-align:center}
.titles{text-align:center;font-size:6.6px;line-height:8px}
.titles .upper{text-transform:uppercase}
.tagbar{position:absolute;left:0;right:0;top:72px;height:14px;background:var(--tagbar);display:flex;justify-content:space-around;align-items:center;padding:0 8px;color:var(--white);font-size:6.6px}
.tagbar span b{color:var(--red);font-weight:400;margin-right:1px}

/* left column */
.sidebar{position:absolute;left:0;top:86px;width:126px;bottom:6px;background:var(--panel)}
.side-block{position:absolute;left:8px;width:113px;font-size:6.1px;line-height:7.3px}
.side-title{color:var(--red);font-weight:600;font-size:7.2px;letter-spacing:.2px;border-bottom:.6px solid var(--red);padding-bottom:1px;margin-bottom:5px}
.contact-row{display:flex;gap:3px;align-items:flex-start}
.contact-dot{flex:0 0 5px;width:5px;height:5px;margin-top:1.2px;border-radius:50%;background:var(--red)}
.contact-row div{white-space:nowrap}
.skills{list-style:none}
.skills li{display:flex;gap:6px;margin-bottom:4.3px;line-height:6.6px}
.skills svg{flex:0 0 6px;width:6px;height:6px;margin-top:.3px}
.skills .region{color:var(--red)}
.memberships{list-style:none}
.memberships li{position:relative;padding-left:5px}
.memberships li::before{content:"•";color:var(--red);position:absolute;left:0}

/* right column */
.timeline-v{position:absolute;left:141px;width:.8px;background:var(--red)}
.timeline-h{position:absolute;height:.8px;background:var(--red)}
.icon-ring{position:absolute;width:24px;height:24px;border-radius:50%;background:var(--white);border:1.2px solid var(--ring);display:flex;align-items:center;justify-content:center}
.section-bar{position:absolute;height:10px;background:var(--red);color:var(--white);font-weight:700;font-size:8.4px;line-height:10px;padding-left:8px;letter-spacing:.3px}
.about{position:absolute;left:152px;top:122px;width:163px;font-size:6.2px;line-height:7.7px;text-align:justify}
.about p{margin-bottom:7.6px}
.edu{position:absolute;left:161px;width:160px;font-size:6.2px;line-height:7.5px}
.edu .degree{color:var(--red)}
.edu .school{font-style:italic}
.edu-badge{position:absolute;left:132px;width:20px;height:20px;border-radius:50%;border:1px solid var(--ring)}
.courses{position:absolute;left:161px;top:409px;width:160px;font-size:6.2px;line-height:7.5px}
.courses h3{color:var(--red);font-weight:600;font-size:6.4px;text-decoration:underline;margin-bottom:7px}
.courses ul{list-style:none}
.courses li{position:relative;padding-left:5px}
.courses li::before{content:"•";color:var(--red);position:absolute;left:0}

/* experience page */
.exp-title-bar{position:absolute;left:34px;top:37px;width:287px;height:10px;background:var(--red);color:var(--white);font-weight:700;font-size:8.4px;line-height:10px;padding-left:7px;letter-spacing:.3px}
.exp-line{position:absolute;left:20px;top:41px;width:.8px;height:410px;background:var(--red)}
.exp-base{position:absolute;left:20px;top:451px;width:301px;height:.8px;background:var(--red)}
.exp-icon{position:absolute;left:9px;width:23px;height:23px;border-radius:50%;background:var(--white);border:1.2px solid var(--ring);display:flex;align-items:center;justify-content:center}
.exp-dot{position:absolute;left:16.5px;width:8px;height:8px;border-radius:50%;background:var(--red)}
.job{position:absolute;left:39px;width:283px;font-size:4.6px;line-height:5.9px}
.job h4{color:var(--red);font-weight:700;font-size:5.6px;line-height:6.8px}
.job .org{color:var(--muted);font-size:5.3px;line-height:6.4px}
.job .org i{font-style:italic}
.job ul{list-style:none;margin-top:5px}
.job li{position:relative;padding-left:4px}
.job li::before{content:"•";color:var(--red);position:absolute;left:0}
</style>
</head>
<body>

<!-- Page: with photo -->
<section class="page page--photo">
  <div class="header-red" style="width:126px"></div>
  <div class="header-light"></div>
  <div class="photo" role="img" aria-label="Portrait photo of Bettina Marlow"></div>
  <div class="abs" style="left:126px;top:7px;width:203px">
    <div class="script-name" style="font-size:27px;line-height:30px;color:var(--red)">Bettina Marlow</div>
  </div>
  <div class="titles abs" style="left:126px;top:41px;width:203px">
    <div class="upper">Senior Manager</div>
    <div class="upper">Organisational Development Director</div>
    <div style="color:var(--red)">(With 15 + years’ experience)</div>
  </div>
  <div class="tagbar"><span><b>#</b>HR Strategy</span><span><b>#</b>HR Daily Operations</span><span><b>#</b>HR Projects</span><span><b>#</b>Talent Management</span><span><b>#</b>Business Solutions</span></div>

  <aside class="sidebar"></aside>
  <div class="side-block" style="top:100px">
    <h2 class="side-title">CONTACT</h2>
    <div class="contact-row"><span class="contact-dot"></span><div>bettinam@marlowadvisory.com</div></div>
    <div class="contact-row"><span class="contact-dot"></span><div>+65 XXXX XXXX</div></div>
    <div class="contact-row"><span class="contact-dot"></span><div>Singapore, 528114</div></div>
    <div class="contact-row"><span class="contact-dot"></span><div>www.bettinamarlow.com/profile<br>-2b7c14</div></div>
  </div>
  <div class="side-block" style="top:162px">
    <h2 class="side-title">PERSONAL DATA</h2>
    <div>Date of Birth: DD Month YYYY</div>
    <div>Nationality: USA</div>
    <div style="font-style:italic;padding-left:5px">(permanent Singapore resident permit)</div>
    <div>Marital Status: XXXX</div>
  </div>
  <div class="side-block" style="top:216px">
    <h2 class="side-title">SKILLS</h2>
    <ul class="skills">
      <li><svg viewBox="0 0 10 10"><rect x=".5" y="2" width="7.5" height="7.5" fill="none" stroke="#f04a50" stroke-width="1"/><path d="M2 5.5l2 2L9.5.8" fill="none" stroke="#f04a50" stroke-width="1.6"/></svg><span>Human Resources Strategy</span></li>
      <li><svg viewBox="0 0 10 10"><rect x=".5" y="2" width="7.5" height="7.5" fill="none" stroke="#f04a50" stroke-width="1"/><path d="M2 5.5l2 2L9.5.8" fill="none" stroke="#f04a50" stroke-width="1.6"/></svg><span>HR Policy</span></li>
      <li><svg viewBox="0 0 10 10"><rect x=".5" y="2" width="7.5" height="7.5" fill="none" stroke="#f04a50" stroke-width="1"/><path d="M2 5.5l2 2L9.5.8" fill="none" stroke="#f04a50" stroke-width="1.6"/></svg><span>Human Resources Operations</span></li>
      <li><svg viewBox="0 0 10 10"><rect x=".5" y="2" width="7.5" height="7.5" fill="none" stroke="#f04a50" stroke-width="1"/><path d="M2 5.5l2 2L9.5.8" fill="none" stroke="#f04a50" stroke-width="1.6"/></svg><span>Consulting,<br>Stakeholder Management</span></li>
      <li><svg viewBox="0 0 10 10"><rect x=".5" y="2" width="7.5" height="7.5" fill="none" stroke="#f04a50" stroke-width="1"/><path d="M2 5.5l2 2L9.5.8" fill="none" stroke="#f04a50" stroke-width="1.6"/></svg><span>Recruitment Process,<br>Talent Acquisition</span></li>
      <li><svg viewBox="0 0 10 10"><rect x=".5" y="2" width="7.5" height="7.5" fill="none" stroke="#f04a50" stroke-width="1"/><path d="M2 5.5l2 2L9.5.8" fill="none" stroke="#f04a50" stroke-width="1.6"/></svg><span>Talent Management,<br>Performance Management,<br>Competency Development</span></li>
      <li><svg viewBox="0 0 10 10"><rect x=".5" y="2" width="7.5" height="7.5" fill="none" stroke="#f04a50" stroke-width="1"/><path d="M2 5.5l2 2L9.5.8" fill="none" stroke="#f04a50" stroke-width="1.6"/></svg><span><span class="region">Singapore,</span><br>Employment Legislation &amp;<br>Industrial Relations.</span></li>
      <li><svg viewBox="0 0 10 10"><rect x=".5" y="2" width="7.5" height="7.5" fill="none" stroke="#f04a50" stroke-width="1"/><path d="M2 5.5l2 2L9.5.8" fill="none" stroke="#f04a50" stroke-width="1.6"/></svg><span><span class="region">Australia,</span><br>Fair Work, National Standards<br>and Awards</span></li>
      <li><svg viewBox="0 0 10 10"><rect x=".5" y="2" width="7.5" height="7.5" fill="none" stroke="#f04a50" stroke-width="1"/><path d="M2 5.5l2 2L9.5.8" fill="none" stroke="#f04a50" stroke-width="1.6"/></svg><span>HR Business Partner</span></li>
      <li><svg viewBox="0 0 10 10"><rect x=".5" y="2" width="7.5" height="7.5" fill="none" stroke="#f04a50" stroke-width="1"/><path d="M2 5.5l2 2L9.5.8" fill="none" stroke="#f04a50" stroke-width="1.6"/></svg><span>HR Project Management</span></li>
    </ul>
  </div>
  <div class="side-block" style="top:406px">
    <h2 class="side-title">PROFESSIONAL MEMBERSHIPS</h2>
    <ul class="memberships">
      <li>Member of Singapore People Management Guild, 104 2217 2020</li>
      <li>Member of Australian People Practice Guild, 385120.</li>
    </ul>
  </div>

  <div class="timeline-v" style="top:104px;height:158px"></div>
  <div class="timeline-h" style="left:141px;top:262px;width:181px"></div>
  <div class="icon-ring" style="left:129.5px;top:92px"><svg width="12" height="12" viewBox="0 0 12 12"><circle cx="6" cy="3.5" r="2.6" fill="#f04a50"/><path d="M1 12c0-3.6 2.2-5.6 5-5.6s5 2 5 5.6z" fill="#f04a50"/></svg></div>
  <h2 class="section-bar" style="left:154px;top:99px;width:168px">ABOUT ME</h2>
  <div class="about">
    <p>My strength is in leadership, developing strategies and providing excellence in HR Operational Services, Recruiting, People Development and building high performing teams to accelerate business performance and drive engagement.</p>
    <p>Masters in Strategic Organisational Development. As an authentic leader I excel at navigating across the business to build a positive culture while consulting with executives to understand imperative businessneeds and recommend the best solution.</p>
    <p>Successfully rolled out Fizzora Project for 200 + new customer sites for the NOVA Perfect OrchardProject and actively recruited for 20 + technical field service agents, developed their capabilities and achieved 100% completion of the project.</p>
  </div>

  <div class="timeline-v" style="top:284px;height:168px"></div>
  <div class="timeline-h" style="left:141px;top:452px;width:181px"></div>
  <div class="icon-ring" style="left:129.5px;top:272px"><svg width="13" height="11" viewBox="0 0 13 11"><path d="M6.5 0L13 3 6.5 6 0 3z" fill="#f04a50"/><path d="M3 4.6v3c1 1.4 5.9 1.4 7 0v-3L6.5 6.3z" fill="#f04a50"/></svg></div>
  <h2 class="section-bar" style="left:154px;top:279px;width:168px">EDUCATION</h2>
  <span class="edu-badge" style="top:300px;background:#1e1e1e"></span>
  <div class="edu" style="top:299px"><div class="degree">Masters in Strategic Organisational Development</div><div class="school">Northgate University, Australia</div><div>December 2011 to December 2017</div></div>
  <span class="edu-badge" style="top:332px;background:#c9a448"></span>
  <div class="edu" style="top:330px"><div class="degree">Management in Human Resources Certificate<br>– Graduated with Distinction</div><div class="school">Pacific State University Extension Program, USA</div><div>June 2003 – November 2006</div></div>
  <span class="edu-badge" style="top:370px;background:#2c8fc4"></span>
  <div class="edu" style="top:368px"><div class="degree">Bachelor of Business in Tourism Management</div><div class="school">Coastal Ridge University, Australia</div><div>January 1992 to December 1996</div></div>
  <div class="courses"><h3>CURRENT COURSES COMPLETED, 2020</h3><ul><li>Singapore Employment Legislation and Industrial Relations, SPMG, 2020.</li><li>Human Resource Analytics and Insights, SPMG, 2020.</li></ul></div>
  <div class="page__footer"></div>
</section>

<!-- Page: without photo -->
<section class="page page--plain">
  <div class="header-red" style="width:329px"></div>
  <div class="abs" style="left:0;top:3px;width:329px">
    <div class="script-name" style="font-size:34px;line-height:40px;color:var(--white)">Bettina Marlow</div>
  </div>
  <div class="titles abs" style="left:0;top:49px;width:329px;color:var(--white)">
    <div class="upper">Senior Manager &nbsp;&nbsp;| &nbsp;&nbsp;Organisational Development Director</div>
    <div>(With 15 + years’ experience)</div>
  </div>
  <div class="tagbar"><span><b>#</b>HR Strategy</span><span><b>#</b>HR Daily Operations</span><span><b>#</b>HR Projects</span><span><b>#</b>Talent Management</span><span><b>#</b>Business Solutions</span></div>

  <aside class="sidebar"></aside>
  <div class="side-block" style="top:100px">
    <h2 class="side-title">CONTACT</h2>
    <div class="contact-row"><span class="contact-dot"></span><div>bettinam@marlowadvisory.com</div></div>
    <div class="contact-row"><span class="contact-dot"></span><div>+65 XXXX XXXX</div></div>
    <div class="contact-row"><span class="contact-dot"></span><div>Singapore, 528114</div></div>
    <div class="contact-row"><span class="contact-dot"></span><div>www.bettinamarlow.com/profile<br>-2b7c14</div></div>
  </div>
  <div class="side-block" style="top:162px">
    <h2 class="side-title">PERSONAL DATA</h2>
    <div>Date of Birth: DD Month YYYY</div>
    <div>Nationality: USA</div>
    <div style="font-style:italic;padding-left:5px">(permanent Singapore resident permit)</div>
    <div>Marital Status: XXXX</div>
  </div>
  <div class="side-block" style="top:216px">
    <h2 class="side-title">SKILLS</h2>
    <ul class="skills">
      <li><svg viewBox="0 0 10 10"><rect x=".5" y="2" width="7.5" height="7.5" fill="none" stroke="#f04a50" stroke-width="1"/><path d="M2 5.5l2 2L9.5.8" fill="none" stroke="#f04a50" stroke-width="1.6"/></svg><span>Human Resources Strategy</span></li>
      <li><svg viewBox="0 0 10 10"><rect x=".5" y="2" width="7.5" height="7.5" fill="none" stroke="#f04a50" stroke-width="1"/><path d="M2 5.5l2 2L9.5.8" fill="none" stroke="#f04a50" stroke-width="1.6"/></svg><span>HR Policy</span></li>
      <li><svg viewBox="0 0 10 10"><rect x=".5" y="2" width="7.5" height="7.5" fill="none" stroke="#f04a50" stroke-width="1"/><path d="M2 5.5l2 2L9.5.8" fill="none" stroke="#f04a50" stroke-width="1.6"/></svg><span>Human Resources Operations</span></li>
      <li><svg viewBox="0 0 10 10"><rect x=".5" y="2" width="7.5" height="7.5" fill="none" stroke="#f04a50" stroke-width="1"/><path d="M2 5.5l2 2L9.5.8" fill="none" stroke="#f04a50" stroke-width="1.6"/></svg><span>Consulting,<br>Stakeholder Management</span></li>
      <li><svg viewBox="0 0 10 10"><rect x=".5" y="2" width="7.5" height="7.5" fill="none" stroke="#f04a50" stroke-width="1"/><path d="M2 5.5l2 2L9.5.8" fill="none" stroke="#f04a50" stroke-width="1.6"/></svg><span>Recruitment Process,<br>Talent Acquisition</span></li>
      <li><svg viewBox="0 0 10 10"><rect x=".5" y="2" width="7.5" height="7.5" fill="none" stroke="#f04a50" stroke-width="1"/><path d="M2 5.5l2 2L9.5.8" fill="none" stroke="#f04a50" stroke-width="1.6"/></svg><span>Talent Management,<br>Performance Management,<br>Competency Development</span></li>
      <li><svg viewBox="0 0 10 10"><rect x=".5" y="2" width="7.5" height="7.5" fill="none" stroke="#f04a50" stroke-width="1"/><path d="M2 5.5l2 2L9.5.8" fill="none" stroke="#f04a50" stroke-width="1.6"/></svg><span><span class="region">Singapore,</span><br>Employment Legislation &amp;<br>Industrial Relations.</span></li>
      <li><svg viewBox="0 0 10 10"><rect x=".5" y="2" width="7.5" height="7.5" fill="none" stroke="#f04a50" stroke-width="1"/><path d="M2 5.5l2 2L9.5.8" fill="none" stroke="#f04a50" stroke-width="1.6"/></svg><span><span class="region">Australia,</span><br>Fair Work, National Standards<br>and Awards</span></li>
      <li><svg viewBox="0 0 10 10"><rect x=".5" y="2" width="7.5" height="7.5" fill="none" stroke="#f04a50" stroke-width="1"/><path d="M2 5.5l2 2L9.5.8" fill="none" stroke="#f04a50" stroke-width="1.6"/></svg><span>HR Business Partner</span></li>
      <li><svg viewBox="0 0 10 10"><rect x=".5" y="2" width="7.5" height="7.5" fill="none" stroke="#f04a50" stroke-width="1"/><path d="M2 5.5l2 2L9.5.8" fill="none" stroke="#f04a50" stroke-width="1.6"/></svg><span>HR Project Management</span></li>
    </ul>
  </div>
  <div class="side-block" style="top:406px">
    <h2 class="side-title">PROFESSIONAL MEMBERSHIPS</h2>
    <ul class="memberships">
      <li>Member of Singapore People Management Guild, 104 2217 2020</li>
      <li>Member of Australian People Practice Guild, 385120.</li>
    </ul>
  </div>

  <div class="timeline-v" style="top:104px;height:158px"></div>
  <div class="timeline-h" style="left:141px;top:262px;width:181px"></div>
  <div class="icon-ring" style="left:129.5px;top:92px"><svg width="12" height="12" viewBox="0 0 12 12"><circle cx="6" cy="3.5" r="2.6" fill="#f04a50"/><path d="M1 12c0-3.6 2.2-5.6 5-5.6s5 2 5 5.6z" fill="#f04a50"/></svg></div>
  <h2 class="section-bar" style="left:154px;top:99px;width:168px">ABOUT ME</h2>
  <div class="about">
    <p>My strength is in leadership, developing strategies and providing excellence in HR Operational Services, Recruiting, People Development and building high performing teams to accelerate business performance and drive engagement.</p>
    <p>Masters in Strategic Organisational Development. As an authentic leader I excel at navigating across the business to build a positive culture while consulting with executives to understand imperative businessneeds and recommend the best solution.</p>
    <p>Successfully rolled out Fizzora Project for 200 + new customer sites for the NOVA Perfect OrchardProject and actively recruited for 20 + technical field service agents, developed their capabilities and achieved 100% completion of the project.</p>
  </div>

  <div class="timeline-v" style="top:284px;height:168px"></div>
  <div class="timeline-h" style="left:141px;top:452px;width:181px"></div>
  <div class="icon-ring" style="left:129.5px;top:272px"><svg width="13" height="11" viewBox="0 0 13 11"><path d="M6.5 0L13 3 6.5 6 0 3z" fill="#f04a50"/><path d="M3 4.6v3c1 1.4 5.9 1.4 7 0v-3L6.5 6.3z" fill="#f04a50"/></svg></div>
  <h2 class="section-bar" style="left:154px;top:279px;width:168px">EDUCATION</h2>
  <span class="edu-badge" style="top:300px;background:#1e1e1e"></span>
  <div class="edu" style="top:299px"><div class="degree">Masters in Strategic Organisational Development</div><div class="school">Northgate University, Australia</div><div>December 2011 to December 2017</div></div>
  <span class="edu-badge" style="top:332px;background:#c9a448"></span>
  <div class="edu" style="top:330px"><div class="degree">Management in Human Resources Certificate<br>– Graduated with Distinction</div><div class="school">Pacific State University Extension Program, USA</div><div>June 2003 – November 2006</div></div>
  <span class="edu-badge" style="top:370px;background:#2c8fc4"></span>
  <div class="edu" style="top:368px"><div class="degree">Bachelor of Business in Tourism Management</div><div class="school">Coastal Ridge University, Australia</div><div>January 1992 to December 1996</div></div>
  <div class="courses"><h3>CURRENT COURSES COMPLETED, 2020</h3><ul><li>Singapore Employment Legislation and Industrial Relations, SPMG, 2020.</li><li>Human Resource Analytics and Insights, SPMG, 2020.</li></ul></div>
  <div class="page__footer"></div>
</section>

<!-- Page: work experience -->
<section class="page page--experience">
  <div class="abs" style="left:0;top:2px;width:329px">
    <div class="script-name" style="font-size:26px;line-height:30px;color:var(--red)">Bettina Marlow</div>
  </div>
  <div class="exp-line"></div>
  <div class="exp-base"></div>
  <div class="exp-icon" style="top:29px"><svg width="12" height="10" viewBox="0 0 12 10"><rect x="0" y="2.5" width="12" height="7.5" rx="1" fill="#f04a50"/><rect x="4" y=".5" width="4" height="2.5" rx=".6" fill="none" stroke="#f04a50" stroke-width="1"/></svg></div>
  <h2 class="exp-title-bar">WORK EXPERIENCE</h2>

  <div class="exp-icon" style="top:57px"><span style="width:9px;height:9px;border-radius:50%;background:var(--red)"></span></div>
  <div class="job" style="top:62px">
    <h4>Senior Manager, Organisational Development Director, Service, FMCG Industry</h4>
    <div class="org">Marlow Advisory <i>(Singapore August 2015 to Present)</i></div>
    <ul>
      <li>Delivered HR Strategy &amp; Daily HR Operations, HR Policy, Recruitment, Performance Management &amp; Communications.</li>
      <li>Leadership, Team Management to 20 + Technical Field Service Agents, FMCG/ F &amp; B Retail Project.</li>
      <li>Recruitment Process for MNCs – Fizzora, Crispo and Bramble for large scale projects.</li>
      <li>HR Advisor to business leaders to achieve business strategic objectives.</li>
      <li>Worked with Senior Leaders in manpower planning, skill development and tracking.</li>
      <li>Developed action plans and strategies to support business needs, talent management, performance management check ins.</li>
      <li>HRBP, Stakeholder Management, Workforce Planning for NOVA Project Roll Out.</li>
      <li>Project P + L Financial Management to $ 1.2 Million SG</li>
      <li>Digitalised business solution of online Service App, digitalised all services improvements to value add, increase efficiencies, transparency and reporting to customers.</li>
      <li>Provide tools required for Team Members and training on new Service App system.</li>
      <li>Manage Performance Management Process check ins, which resulted in greater levels of engagement</li>
      <li>Identify, source, interview, select the right talent to service 200 equipment assets/per month ie. 400+ field services performed each month and efficient operational call outs.</li>
      <li>Oversee weekly payroll and summary report. Sign off on PAYG Tax and GST Report</li>
      <li>Educated new hires on expected job tasks, compensation and benefits to set clear expectations.</li>
      <li>Coaching on expected behaviours through consultations, job spec and code of business reference.</li>
      <li>Project Management - resourcing &amp;operational requirements regards to the roll out of Fizzora &amp; Crispo Technical Field Services for 200 equipment machines assets per month to deliver positive customer service results.</li>
    </ul>
  </div>

  <div class="exp-icon" style="top:195px"><span style="width:9px;height:9px;border-radius:50%;background:#1f3f8f"></span></div>
  <div class="job" style="top:201px">
    <h4>Organisational Development Director, Client Relations.</h4>
    <div class="org">Brightwell Pty. Ltd <i>(Australia, June 2008 to August 2015)</i></div>
    <ul>
      <li>Established Business Strategy in consultation with management.</li>
      <li>Delivered HR Strategy and daily hands on Human Resources Operations:<br>Recruitment,Performance Management and Training and Development.</li>
      <li>Leadership to Team of 20 + resources, created a high performing service focused team.</li>
      <li>Client relations, effective communications and stakeholder management.</li>
      <li>Managed recruitment process for Equipment Field Services Team for Multi National Client Projects: Fizzora, Crispo and Bramble.</li>
      <li>Recruit new Service Provider contracts with Fizzora, Crispo, Goldbun and Bramble.</li>
      <li>Project P + L Financial Management to $ 1.2m SG</li>
      <li>Workforce Planning on Technical Field Projects for Fizzora and Crispo for resources across NSW, QLD, VIC and SA for &gt; 200 services equipment assets, 400 + operational field services performed per month.</li>
      <li>Focused on quality service results, delivering a positive customer service experience.</li>
    </ul>
  </div>

  <div class="exp-icon" style="top:290px"><span style="width:9px;height:9px;border-radius:50%;border:1.6px solid #1a9bb8"></span></div>
  <div class="job" style="top:295px">
    <h4>Director Career Services.</h4>
    <div class="org">Harbourline College <i>(USA, October 2003 to December 2007)</i></div>
    <ul>
      <li>Brand expansion, Business Development, Marketing of Harbourline College into San Francisco, Sacramento, Fremont, Santa Clara and the Bay Area.</li>
      <li>Built out the department from scratch, developed strategies, process and service standards.</li>
      <li>HR Strategy and Human Resource Operations: Recruitment, Job Placement, Performance Management, HR Policy, Training and Development.</li>
      <li>Graduate Program Placement for 700 + Medical graduates, MA, LVN and RN Program.</li>
      <li>Acquired new accounts from multiple hospitals and medical centres across the San Francisco Bay Area.</li>
      <li>Project Management with Senior Leadership Team for Board of Private Education Accreditation Business Goal, engagement and contracts for preceptorships sites to facilitate L &amp; D.</li>
      <li>Awarded 2005 - Employee of the Year</li>
      <li>Account Management: Redwood Health, Oakmere Medical Centre, Valleyview Medical Centre and Bayside Veterans Care Network.</li>
    </ul>
  </div>

  <span class="exp-dot" style="top:390px"></span>
  <div class="job" style="top:388px"><h4>Recruitment Consultant</h4><div class="org">Tandem Staffing, Health Care and IT Industry <i>(Australia, July 2002 to April 2003)</i></div></div>
  <span class="exp-dot" style="top:409px"></span>
  <div class="job" style="top:408px"><h4>Recruitment Consultant</h4><div class="org">Netwave, IT Industry <i>(Australia, July 2001 to May 2002)</i></div></div>
  <span class="exp-dot" style="top:429px"></span>
  <div class="job" style="top:428px"><h4>Sales and IT Sourcer</h4><div class="org">Corelink Systems, IT Industry <i>(Australia, April 2000 to April 2001)</i></div></div>

  <div class="page__footer"></div>
</section>

</body>
</html>
```